Business Card Design

A business card design must match as a cleaning company.
We do house cleaning, office, cafe , function center , club and so on.

Industry/Entity Type

House

Contact Information for Business Card

Bright Lane cleaning services
Mara Delvin
Director
0428395146
1300 917 254
Brightlane.cleaning@bluvex.com

```html
<!DOCTYPE html>
<html lang="en">
<head>
<meta charset="utf-8">
<title>Bright Lane Cleaning Services – Business Card</title>
<link href="https://fonts.googleapis.com/css2?family=Exo+2:wght@400;600;700;800&family=Michroma&display=swap" rel="stylesheet">
<style>
  :root {
    --page: #ebe7e1;
    --blue: #1a80c4;
    --blue-deep: #0c62a0;
    --green: #6ba322;
    --white: #ffffff;
    --ink: #1b1b1b;
    --logo-blue: #1671b4;
  }
  * { margin: 0; padding: 0; box-sizing: border-box; }
  html, body { width: 1200px; height: 1050px; overflow: hidden; }
  body { background: var(--page); font-family: "Exo 2", sans-serif; }

  .card {
    position: absolute; left: 320px; top: 35px;
    width: 560px; height: 980px;
    background: radial-gradient(circle at 60% 40%, var(--blue) 0%, var(--blue-deep) 100%);
    box-shadow: 0 12px 30px rgba(0,0,0,0.25);
    overflow: hidden;
  }
  .card__top-stripe { position: absolute; left: 0; top: 0; width: 100%; height: 18px; background: var(--blue); }
  .card__top-rule { position: absolute; left: 0; top: 18px; width: 100%; height: 8px; background: var(--green); }
  .card__header {
    position: absolute; left: 0; top: 26px; width: 100%; height: 176px;
    background: var(--white);
    display: flex; align-items: center; padding-left: 40px; gap: 22px;
  }
  .card__header-rule { position: absolute; left: 0; top: 202px; width: 100%; height: 10px; background: var(--green); }

  .brand__dot { width: 64px; height: 64px; border-radius: 50%; background: var(--logo-blue); flex: none; }
  .brand__name {
    font-family: "Michroma", sans-serif; color: var(--logo-blue);
    font-size: 30px; line-height: 1.15; letter-spacing: 1px;
  }
  .brand__name small { display: block; font-size: 17px; letter-spacing: 2px; }

  .connectors { position: absolute; left: 0; top: 0; width: 560px; height: 980px; }

  .info-box {
    position: absolute; border: 2px solid var(--white);
    color: var(--white); text-align: center;
    display: flex; flex-direction: column; justify-content: center;
  }
  .info-box__label { font-weight: 800; font-size: 24px; letter-spacing: 1px; text-transform: uppercase; }
  .info-box__value { font-size: 19px; margin-top: 6px; letter-spacing: 0.5px; }

  .info-box--name { left: 230px; top: 240px; width: 300px; height: 100px; background: var(--white); color: var(--ink); }
  .info-box--name .person { font-family: "Exo 2", sans-serif; font-weight: 800; font-size: 30px; letter-spacing: 1px; text-transform: uppercase; }
  .info-box--name .role { font-size: 18px; margin-top: 2px; }
  .info-box--phone { left: 190px; top: 380px; width: 320px; height: 100px; }
  .info-box--email { left: 150px; top: 520px; width: 340px; height: 100px; }
  .info-box--email .info-box__value { font-size: 16px; }
  .info-box--web { left: 110px; top: 660px; width: 360px; height: 100px; }

  .card__address {
    position: absolute; left: 0; top: 860px; width: 100%; height: 120px;
    background: var(--green); color: var(--white);
    font-family: "Michroma", sans-serif; font-size: 17px;
    display: flex; align-items: center; padding-left: 32px;
  }
</style>
</head>
<body>
  <div class="card">
    <div class="card__top-stripe"></div>
    <div class="card__top-rule"></div>
    <header class="card__header">
      <span class="brand__dot"></span>
      <div class="brand__name">Bright Lane<small>Cleaning Services</small></div>
    </header>
    <div class="card__header-rule"></div>

    <svg class="connectors" viewBox="0 0 560 980" aria-hidden="true">
      <g stroke="#ffffff" stroke-width="2" fill="none">
        <line x1="50" y1="250" x2="50" y2="710"/>
        <line x1="50" y1="250" x2="230" y2="250"/>
        <line x1="50" y1="430" x2="190" y2="430"/>
        <line x1="50" y1="570" x2="150" y2="570"/>
        <line x1="50" y1="710" x2="110" y2="710"/>
      </g>
    </svg>

    <div class="info-box info-box--name">
      <span class="person">Mara Delvin</span>
      <span class="role">Managing Director</span>
    </div>
    <div class="info-box info-box--phone">
      <span class="info-box__label">Phone</span>
      <span class="info-box__value">0428395146</span>
    </div>
    <div class="info-box info-box--email">
      <span class="info-box__label">Email</span>
      <span class="info-box__value">Brightlane.cleaning@bluvex.com</span>
    </div>
    <div class="info-box info-box--web">
      <span class="info-box__label">Website</span>
      <span class="info-box__value">www.brightlaneclean.com</span>
    </div>

    <footer class="card__address">27.14th floor,Harbour Point Road KLV</footer>
  </div>
</body>
</html>
```